New Wordpress Design Project: TR- Tamberly Roots, Training Beyond Equity, Diversity, and Inclusion

I need a clean, modern, website design for TR- a national consulting firm providing equity, diversity, and inclusion training, through the lens of undoing racism, for arts and culture, and the non profit industry. It will feature both written posts, and some video. People will need TR contact information, and subscribe to receive information. It will feature a pretty active blog, and a section for resources, with links to other sites. There needs to be a section about TR,its training, approach, and bio Information. I probably should have put this first!

I want a site that draws people in. That is interesting and dynamic. My approach to this work is to provide people with the information, knowledge, and tools they need to go back to their communities and do the work. So they are at the center of the story. And I like powerful imagery. It could also be pretty.

The idea of undoing racism is a big idea. It is powerful, heroic even. And thousands of people in the US are working hard to do just that. So there is a sense of movement building here, of connecting to something important.

I already have a logo design that was done through a contest here last month.

Target Market(s)

Arts and culture fields, non profit industry, and philanthropy

Font styles to use
Sans Serif

Requirements
Must have
• Must have dynamic powerful imagery, be clean and easy to navigate, support concept of story telling, good use of color, be inviting, draw people in to learn when they see it first time. The ability to update photos, and videos easily. Connect to social media, especially Pinglomar and Tallyhive.
Nice to have
• It would be nice to have a website that uses more images than words to tell stories. I don't know enough about what's possible in website design to add more to this section.
Should not have
• Should not look like we are selling products, or services even but, rather, providing essential information and knowledge to help people make this world a better place for more people.

```html
<!DOCTYPE html>
<html lang="en">
<head>
<meta charset="utf-8">
<title>Tamberly Roots — Training Beyond Equity, Diversity, and Inclusion</title>
<link rel="stylesheet" href="https://fonts.googleapis.com/css2?family=Open+Sans:wght@400;600;700&display=swap">
<style>
  :root{
    --yellow:#f7cc0a;
    --yellow-text:#efc10b;
    --dark:#2b2b2b;
    --darker:#222222;
    --ink:#333333;
    --muted:#7d7d7d;
    --rule:#d9d9d9;
    --soft-bg:#fafafa;
    --white:#ffffff;
  }
  *{box-sizing:border-box;margin:0;padding:0}
  html,body{width:1200px;height:2230px;overflow:hidden}
  body{font-family:"Open Sans",Arial,sans-serif;color:var(--ink);background:var(--white);position:relative}
  .container{width:800px;margin:0 auto;position:relative}

  /* Header */
  .site-header{height:95px;background:linear-gradient(#303030,#262626);position:relative}
  .brand{position:absolute;left:200px;top:30px;display:flex;align-items:center;gap:10px;color:var(--white);font-size:17px;font-weight:600}
  .brand-dot{width:22px;height:22px;border-radius:50%;background:var(--yellow)}
  .top-contact{position:absolute;right:200px;top:17px;display:flex;align-items:center;gap:22px;color:var(--white);font-size:11px}
  .top-contact span{display:flex;align-items:center;gap:8px}
  .search-btn{width:21px;height:21px;border-radius:50%;background:var(--yellow);display:flex;align-items:center;justify-content:center}
  .main-nav{position:absolute;right:200px;top:56px;display:flex;gap:25px;font-size:11px;color:var(--white);text-transform:uppercase}
  .main-nav .active{color:var(--yellow)}

  /* Hero */
  .hero{height:452px;position:relative;background:linear-gradient(100deg,#3a3029 0%,#4b4036 30%,#3b3a3c 55%,#5a5040 80%,#6b5a2c 100%)}
  .hero-arrow{position:absolute;top:276px;width:46px;height:46px;border-radius:50%;border:1px solid rgba(255,255,255,.7);display:flex;align-items:center;justify-content:center}
  .hero-arrow.prev{left:32px;top:276px;background:rgba(0,0,0,.25)}
  .hero-arrow.next{right:32px;background:rgba(0,0,0,.25)}
  .hero-arrow{top:181px}
  .hero-copy{position:absolute;left:605px;top:140px;color:var(--white);width:400px}
  .hero-copy h1{font-size:47px;font-weight:400;letter-spacing:.5px;line-height:1.1}
  .hero-copy p{font-size:14px;line-height:22px;margin-top:14px}
  .btn{display:inline-block;background:var(--yellow);color:var(--white);font-weight:600;text-transform:uppercase}
  .hero-copy .btn{margin-top:18px;font-size:13px;padding:10px 22px}

  /* Section headings */
  .section-title{text-align:center;color:var(--yellow-text);font-size:22px;font-weight:400;text-transform:uppercase}
  .section-sub{text-align:center;color:var(--muted);font-size:13px;margin-top:14px}
  .dashed{border-top:1px dashed var(--rule)}

  /* Intro */
  .intro{padding-top:78px}
  .intro .dashed.first{margin-top:34px}
  .pillars{display:flex;justify-content:space-between;padding:38px 0 50px}
  .pillar{width:250px}
  .pillar-head{display:flex;align-items:center;gap:12px;font-size:13px;font-weight:600;color:var(--ink);text-transform:uppercase}
  .pillar-bar{width:40px;height:3px;background:var(--yellow);margin-top:6px}
  .pillar p{color:var(--muted);font-size:13px;line-height:22.5px;margin-top:30px}

  /* Blog */
  .blog{padding-top:62px;height:482px}
  .cards{display:flex;justify-content:space-between;margin-top:38px}
  .post-card{width:253px;height:236px;position:relative;box-shadow:0 4px 6px rgba(0,0,0,.12)}
  .post-card.coins{background:linear-gradient(160deg,#b9a27a,#8a7452 60%,#5d4c36)}
  .post-card.city{background:linear-gradient(160deg,#2a3f66,#243556 55%,#1a2540)}
  .post-card.chart{background:linear-gradient(160deg,#1f4f80,#163c66 55%,#0f2a4a)}
  .post-date{position:absolute;left:77px;top:75px;width:83px;height:72px;background:var(--yellow);color:var(--white);font-size:12px;line-height:13px;text-align:center;padding-top:14px;text-transform:uppercase}
  .post-excerpt{position:absolute;left:20px;right:20px;top:155px;color:var(--white);font-size:10px;line-height:14px;text-align:center}
  .play{position:absolute;right:16px;bottom:10px;width:26px;height:18px;border:1px solid var(--white);display:flex;align-items:center;justify-content:center}

  /* Resources */
  .resources{background:var(--soft-bg);height:476px;padding-top:62px;border-top:1px dashed var(--rule)}
  .resource-list{display:flex;justify-content:space-between;margin-top:38px}
  .resource{width:253px}
  .resource-thumb{height:150px}
  .resource-thumb.tech{background:linear-gradient(135deg,#233a6e,#4f6fb0 50%,#8a6f9a)}
  .resource-thumb.desk{background:linear-gradient(135deg,#c99a55,#e5d2b5 50%,#bfb3a3)}
  .resource-thumb.graph{background:linear-gradient(135deg,#1c4f9a,#3a7fd0 55%,#1a3a75)}
  .resource-link{font-size:10px;color:var(--ink);margin-top:20px;padding-left:2px}
  .resource p{color:var(--muted);font-size:13px;line-height:22px;margin-top:8px}
  .resource .btn{font-size:7px;padding:7px 17px;margin-top:16px}

  /* Footer */
  .site-footer{height:294px;background:linear-gradient(#2b2b2b,#232323);color:var(--white);position:relative}
  .footer-brand{position:absolute;left:200px;top:44px;display:flex;align-items:center;gap:8px;font-size:14px;font-weight:600}
  .footer-col{position:absolute;top:44px}
  .footer-col h3{color:var(--yellow);font-size:13px;font-weight:600;text-transform:uppercase}
  .col-links{left:361px}
  .col-links ul{list-style:none;margin-top:22px;font-size:10px;line-height:22.4px;text-transform:uppercase}
  .col-contact{left:532px}
  .contact-name{font-size:13px;margin-top:24px;text-transform:uppercase}
  .contact-role{font-size:8px;color:#aaaaaa;margin-top:10px;text-transform:uppercase}
  .contact-line{display:flex;align-items:center;gap:9px;font-size:10px;margin-top:18px;text-transform:uppercase}
  .col-subscribe{left:749px;width:251px}
  .col-subscribe p{font-size:10px;line-height:22px;margin-top:22px;text-transform:uppercase}
  .email-field{margin-top:14px;height:28px;border:1px solid #555;font-size:8px;color:#999;padding:9px 8px}
  .col-subscribe .btn{margin-top:14px;font-size:10px;padding:6px 12px;color:var(--darker)}
  .footer-bottom{position:absolute;left:200px;right:200px;top:2208px;}
  .copyright{position:absolute;left:200px;top:264px;font-size:10px}
  .social{position:absolute;left:614px;top:264px;font-size:10px;display:flex;gap:12px;text-transform:uppercase}
  .social .net{color:var(--yellow)}
  .legal{position:absolute;right:200px;top:264px;font-size:10px;text-transform:uppercase}
</style>
</head>
<body>

<header class="site-header">
  <div class="brand"><span class="brand-dot"></span>Tamberly Roots</div>
  <div class="top-contact">
    <span>
      <svg width="11" height="8" viewBox="0 0 11 8"><rect x=".5" y=".5" width="10" height="7" fill="none" stroke="#f7cc0a"/><path d="M.5 .5 5.5 4.5 10.5 .5" fill="none" stroke="#f7cc0a"/></svg>
      hello@tamberlyroots.org
    </span>
    <span>
      <svg width="10" height="10" viewBox="0 0 10 10"><path d="M2 0 4 2.5 3 4a6 6 0 0 0 3 3l1.5-1L10 8 8.5 10C4 10 0 6 0 1.5Z" fill="#f7cc0a"/></svg>
      555-014-2290
    </span>
    <span class="search-btn">
      <svg width="10" height="10" viewBox="0 0 10 10"><circle cx="4" cy="4" r="3" fill="none" stroke="#fff" stroke-width="1.5"/><path d="M6.2 6.2 9 9" stroke="#fff" stroke-width="1.5"/></svg>
    </span>
  </div>
  <nav class="main-nav">
    <span class="active">Home</span><span>About Us</span><span>Services</span><span>Blog</span><span>Videos</span><span>Resources</span><span>Contact Us</span>
  </nav>
</header>

<section class="hero" role="img" aria-label="Smiling young man in a work shirt, leaning forward in a warehouse workshop">
  <div class="hero-arrow prev"><svg width="10" height="14" viewBox="0 0 10 14"><path d="M8 1 2 7l6 6" fill="none" stroke="#f7cc0a" stroke-width="2"/></svg></div>
  <div class="hero-arrow next"><svg width="10" height="14" viewBox="0 0 10 14"><path d="M2 1l6 6-6 6" fill="none" stroke="#f7cc0a" stroke-width="2"/></svg></div>
  <div class="hero-copy">
    <h1>TAMBERLY ROOTS</h1>
    <p>Neque porro quisquam est qui dolorem ipsum quia dolor sit amet, consectetur, adipisci velit...</p>
    <span class="btn">Learn More</span>
  </div>
</section>

<section class="intro container">
  <h2 class="section-title">We are a national consulting firm providing</h2>
  <p class="section-sub">Neque porro quisquam est qui dolorem ipsum quia dolor sit amet</p>
  <div class="dashed first"></div>
  <div class="pillars">
    <div class="pillar">
      <div class="pillar-head">
        <svg width="36" height="32" viewBox="0 0 36 32"><g fill="none" stroke="#222" stroke-width="2"><rect x="2" y="4" width="5" height="26"/><rect x="10" y="12" width="5" height="18"/><rect x="18" y="16" width="5" height="14"/><rect x="26" y="20" width="5" height="10"/><path d="M0 31h36"/></g></svg>
        Equity
      </div>
      <div class="pillar-bar"></div>
      <p>Sed ut perspiciatis unde omnis iste natus error sit voluptatem accusantium doloremque laudantium, totam rem aperiam, eaque ipsa quae</p>
    </div>
    <div class="pillar">
      <div class="pillar-head">
        <svg width="26" height="36" viewBox="0 0 26 36"><g fill="none" stroke="#222" stroke-width="2"><path d="M8 26c0-5-6-7-6-14a11 11 0 0 1 22 0c0 7-6 9-6 14Z"/><path d="M9 30h8M10 34h6M13 26v-9l-3-3M13 17l3-3"/></g></svg>
        Diversity
      </div>
      <div class="pillar-bar"></div>
      <p>Sed ut perspiciatis unde omnis iste natus error sit voluptatem accusantium doloremque laudantium, totam rem aperiam, eaque ipsa quae</p>
    </div>
    <div class="pillar">
      <div class="pillar-head">
        <svg width="40" height="30" viewBox="0 0 40 30"><g fill="none" stroke="#222" stroke-width="2"><rect x="1" y="1" width="38" height="28"/><path d="M1 7h38M6 13h28M6 18h28M6 23h20"/></g></svg>
        Inclusion Training
      </div>
      <div class="pillar-bar"></div>
      <p>Sed ut perspiciatis unde omnis iste natus error sit voluptatem accusantium doloremque laudantium, totam rem aperiam, eaque ipsa quae</p>
    </div>
  </div>
  <div class="dashed"></div>
</section>

<section class="blog container">
  <h2 class="section-title">Blog Posts</h2>
  <p class="section-sub">Neque porro quisquam est qui dolorem ipsum quia dolor sit amet</p>
  <div class="cards">
    <article class="post-card coins" role="img" aria-label="Hand stacking coins beside a clock">
      <div class="post-date">Dec<br>12th<br>2016</div>
      <p class="post-excerpt">At vero eos et accusamus et iusto odio dignissimos ducimus qui blanditiis</p>
      <div class="play"><svg width="8" height="10" viewBox="0 0 8 10"><path d="M0 0l8 5-8 5Z" fill="#fff"/></svg></div>
    </article>
    <article class="post-card city" role="img" aria-label="Night city skyline overlaid with market charts">
      <div class="post-date">Dec<br>12th<br>2016</div>
      <p class="post-excerpt">At vero eos et accusamus et iusto odio dignissimos ducimus qui blanditiis</p>
    </article>
    <article class="post-card chart" role="img" aria-label="Businessman touching a glowing stock chart">
      <div class="post-date">Dec<br>12th<br>2016</div>
      <p class="post-excerpt">At vero eos et accusamus et iusto odio dignissimos ducimus qui blanditiis</p>
      <div class="play"><svg width="8" height="10" viewBox="0 0 8 10"><path d="M0 0l8 5-8 5Z" fill="#fff"/></svg></div>
    </article>
  </div>
</section>

<section class="resources">
  <div class="container">
    <h2 class="section-title">Our Resources</h2>
    <p class="section-sub">Neque porro quisquam est qui dolorem ipsum quia dolor sit amet</p>
    <div class="resource-list">
      <div class="resource">
        <div class="resource-thumb tech" role="img" aria-label="Hand touching a digital private equity interface"></div>
        <p class="resource-link">www.linkfieldguide.com/what-is-link-equity/</p>
        <p>Sed ut perspiciatis unde omnis iste natus error sit voluptatem</p>
        <span class="btn">Read More</span>
      </div>
      <div class="resource">
        <div class="resource-thumb desk" role="img" aria-label="Person writing notes over printed charts at a desk"></div>
        <p class="resource-link">www.linkfieldguide.com/what-is-link-equity/</p>
        <p>Sed ut perspiciatis unde omnis iste natus error sit voluptatem</p>
        <span class="btn">Read More</span>
      </div>
      <div class="resource">
        <div class="resource-thumb graph" role="img" aria-label="Rising blue arrow and falling red arrow over a chart"></div>
        <p class="resource-link">www.linkfieldguide.com/what-is-link-equity/</p>
        <p>Sed ut perspiciatis unde omnis iste natus error sit voluptatem</p>
        <span class="btn">Read More</span>
      </div>
    </div>
  </div>
</section>

<footer class="site-footer">
  <div class="footer-brand"><span class="brand-dot"></span>Tamberly Roots</div>
  <div class="footer-col col-links">
    <h3>Other Links</h3>
    <ul><li>Home</li><li>About Us</li><li>Services</li><li>Blog</li><li>Videos</li><li>Resources</li><li>Contact Us</li></ul>
  </div>
  <div class="footer-col col-contact">
    <h3>Contact Us</h3>
    <p class="contact-name">Marisol Denby</p>
    <p class="contact-role">President</p>
    <p class="contact-line"><svg width="10" height="10" viewBox="0 0 10 10"><path d="M2 0 4 2.5 3 4a6 6 0 0 0 3 3l1.5-1L10 8 8.5 10C4 10 0 6 0 1.5Z" fill="#f7cc0a"/></svg>555-014-2290</p>
    <p class="contact-line"><svg width="10" height="10" viewBox="0 0 10 10"><path d="M2 0 4 2.5 3 4a6 6 0 0 0 3 3l1.5-1L10 8 8.5 10C4 10 0 6 0 1.5Z" fill="#f7cc0a"/></svg>hello@tamberlyroots.org</p>
  </div>
  <div class="footer-col col-subscribe">
    <h3>Subscribe to receive information</h3>
    <p>Sed ut perspiciatis unde omnis iste natus error sit voluptatem</p>
    <div class="email-field">Enter Your E-mail Address</div>
    <span class="btn">Subscribe Now</span>
  </div>
  <p class="copyright">© 2016 COMPANY NAME &nbsp;|&nbsp; ALL RIGHTS RESERVED</p>
  <p class="social">Connect with us <span class="net">Pinglomar</span><span class="net">Tallyhive</span></p>
  <p class="legal">Terms of Use &nbsp;|&nbsp; Privacy Policy</p>
</footer>

</body>
</html>
```